Bag packaging design of sliced bread

The project is for design of line of sliced bread with different flavours. The brand of the bread will be "Valorina". The shape of the bread will be oval. The bread will be packed in a bag. I attach the layout of the bag. The bag will be closed with a plastic clip. I attach images of similar products. The idea is to have one main design and then each colour to be different type of bread like those in the images 2 and 5.

```html
<!DOCTYPE html>
<html lang="en">
<head>
<meta charset="utf-8">
<title>Valorina Sliced Bread – Bag Label</title>
<link rel="stylesheet" href="https://fonts.googleapis.com/css2?family=Forum&family=Open+Sans:wght@400;600&display=swap">
<style>
  :root {
    --backdrop: #c9b3a3;
    --bag-film: #f4efe9;
    --crumb-light: #e8c889;
    --crumb-dark: #9a6535;
    --window-orange: #f39a2c;
    --ribbon-orange: #e98a14;
    --ribbon-deep: #c96f0a;
    --badge-brown: #5a3728;
    --badge-rim: #f7a21e;
    --label-cream: #f5efe8;
    --brand-brown: #6b4030;
    --stripe-brown: #7a4a35;
    --stripe-yellow: #fcc21b;
    --stripe-gold: #f4a514;
    --text-light: #ffffff;
  }
  * { margin: 0; padding: 0; box-sizing: border-box; }
  html, body {
    width: 1200px; height: 642px; overflow: hidden;
    background: var(--backdrop);
  }
  .bag-label { display: block; width: 1200px; height: 642px; }
  .bag-outline { fill: var(--bag-film); }
  .window-panel { fill: var(--window-orange); opacity: .92; }
  .ribbon-band { fill: var(--ribbon-orange); }
  .ribbon-tail { fill: var(--ribbon-deep); }
  .badge-rim { fill: var(--badge-rim); }
  .badge-body { fill: var(--badge-brown); }
  .brand-band { fill: var(--label-cream); }
  .neck-film { fill: var(--bag-film); opacity: .85; }
  .stripe-brown { fill: var(--stripe-brown); }
  .stripe-yellow { fill: var(--stripe-yellow); }
  .stripe-gold { fill: var(--stripe-gold); }
  .product-title {
    font-family: "Forum", serif;
    font-size: 56px;
    letter-spacing: 2px;
    fill: var(--text-light);
  }
  .tagline {
    font-family: "Open Sans", sans-serif;
    font-size: 18px;
    fill: var(--text-light);
  }
  .brand-name {
    font-family: "Open Sans", sans-serif;
    font-weight: 600;
    font-size: 40px;
    fill: var(--brand-brown);
  }
</style>
</head>
<body>
<svg class="bag-label" viewBox="0 0 1200 642" xmlns="http://www.w3.org/2000/svg">
  <defs>
    <linearGradient id="crumb" x1="0" y1="0" x2="0" y2="1">
      <stop offset="0" stop-color="var(--crumb-dark)"/>
      <stop offset=".55" stop-color="#c79a5e"/>
      <stop offset="1" stop-color="var(--crumb-light)"/>
    </linearGradient>
  </defs>

  <!-- bag body -->
  <rect class="bag-outline" x="55" y="45" width="900" height="450" rx="110"/>
  <rect x="80" y="58" width="855" height="424" rx="95" fill="url(#crumb)"
        role="img" aria-label="Photograph of the sliced oval loaf seen through the clear bag"/>

  <!-- neck and closure stripes -->
  <path class="neck-film" d="M945 205 L975 200 L1140 115 L1160 140 L1160 410 L1140 420 L975 335 L945 330 Z"/>
  <rect class="stripe-brown" x="1040" y="120" width="42" height="300"/>
  <rect class="stripe-yellow" x="1082" y="120" width="18" height="300"/>
  <rect class="stripe-gold" x="1082" y="200" width="18" height="120"/>
  <rect class="stripe-brown" x="1100" y="120" width="12" height="300"/>

  <!-- product window -->
  <rect class="window-panel" x="250" y="88" width="255" height="345" rx="18"/>

  <!-- cream brand band -->
  <path class="brand-band" d="M600 110 L905 130 Q945 135 945 175 L945 225 L955 230 L955 285 L945 290 L945 350 Q945 385 905 388 L600 400 Z"/>

  <!-- ribbon -->
  <path class="ribbon-tail" d="M545 55 L610 95 L610 455 L545 490 Z"/>
  <path class="ribbon-band" d="M500 115 Q470 270 500 425 L560 460 Q610 270 560 80 Z"/>
  <text class="tagline" transform="translate(495 183) rotate(90)">100% natural</text>

  <!-- scalloped badge -->
  <path class="badge-rim" d="M605 98 Q640 82 660 110 Q700 110 715 140 Q752 150 748 190 Q768 215 748 245 Q766 270 748 298 Q762 330 735 352 Q735 390 700 400 Q680 430 645 420 Q615 435 590 420 Q535 430 535 380 L535 140 Q540 100 605 98 Z"/>
  <path class="badge-body" d="M608 107 Q640 94 656 118 Q694 118 707 146 Q740 156 738 192 Q756 215 738 245 Q755 270 738 296 Q750 326 727 346 Q726 380 695 390 Q677 416 646 410 Q616 424 592 410 Q545 418 545 375 L545 145 Q550 110 608 107 Z"/>
  <text class="product-title" transform="translate(670 150) rotate(90)">SLICED</text>
  <text class="product-title" transform="translate(598 150) rotate(90)">BREAD</text>

  <!-- brand name -->
  <text class="brand-name" transform="translate(835 160) rotate(90)">Valorina</text>
</svg>
</body>
</html>
```